2 Wine Label Designs

Amberly Cellars has been helping people give customized wine gifts since 1999. From large scale corporate clients, to 1 bottle personalized gifts, we offer a wide range of wines and templates for any occasion. Recently we’ve started to shift our focus to a younger demographic (21 to 35 year old women) and are in the process of updating our website and branding.

One big area we’re working to improve is the customizable wine label/engraving templates we offer on the site (to see our current template library go to www.amberlycellars.com/shop/wine, select a wine, choose “label” or “engraving” from the dropdown, and click “customize”). You’ll find that a lot of our current templates are outdated or aimed at an older demographic. Over the next few months we want to swap out most of these old templates with fun fresh designs.

We're asking designers to submit 2 customizable wine label templates for this project. One should be wedding themed and the other "Thank You" themed. Please see the attached PDF for more guidelines and creative direction.

Keep in mind, even if you aren't selected as the winner of this project we are going to go through and offer $50 for any label template submitted that we like ($100 if we want both). So there is a good chance you'll be getting some money for your work!

Please read though the attached guidelines PDF carefully (especially the "Must be Customizable" section).

Target Market(s)

21 to 35 year old women

Colors

Designer to choose colors to be used in the design.

Requirements
Must have
• See attached PDF
Nice to have
• See attached PDF
Should not have
• See attached PDF

```html
<!DOCTYPE html>
<html lang="en">
<head>
<meta charset="utf-8">
<title>Wine Labels – Wedding and Thank You</title>
<link href="https://fonts.googleapis.com/css2?family=Homemade+Apple&family=Great+Vibes&display=swap" rel="stylesheet">
<style>
  :root {
    --backdrop: #665253;
    --ink: #5e4a48;
    --ribbon: #ffffff;
    --rose: #f0a3a8;
    --peach: #f6c49a;
    --sky: #a9d8f0;
    --butter: #f7f1b8;
    --sage: #d9e8b6;
    --blush: #f4c8bb;
    --cream: #f8eee2;
    --mint: #cfe9e2;
  }
  html, body {
    margin: 0;
    width: 1200px;
    height: 793px;
    overflow: hidden;
    background: var(--backdrop);
  }
  .canvas {
    position: relative;
    width: 1200px;
    height: 793px;
  }
  .label {
    position: absolute;
    top: 58px;
    height: 679px;
    overflow: hidden;
  }
  .label--wedding { left: 58px; width: 526px; }
  .label--thanks { left: 611px; width: 528px; }

  .wedding-art {
    position: absolute;
    inset: 0;
    background:
      radial-gradient(ellipse 60% 22% at 40% 6%, var(--rose) 0%, transparent 70%),
      radial-gradient(ellipse 55% 20% at 45% 95%, var(--rose) 0%, transparent 70%),
      radial-gradient(ellipse 30% 18% at 92% 92%, var(--peach) 0%, transparent 75%),
      radial-gradient(ellipse 45% 45% at 85% 45%, var(--sky) 0%, transparent 75%),
      radial-gradient(ellipse 45% 30% at 20% 60%, var(--butter) 0%, transparent 80%),
      radial-gradient(ellipse 30% 20% at 8% 80%, var(--sage) 0%, transparent 80%),
      linear-gradient(180deg, #f7d3cf 0%, #f9ecd6 40%, #f6f2c8 70%, #f3d8c2 100%);
  }
  .thanks-art {
    position: absolute;
    inset: 0;
    background:
      radial-gradient(ellipse 40% 50% at 55% 25%, #f2b6a2 0%, transparent 75%),
      radial-gradient(ellipse 35% 40% at 85% 40%, #fbf6f0 0%, transparent 75%),
      radial-gradient(ellipse 25% 25% at 35% 70%, var(--mint) 0%, transparent 75%),
      radial-gradient(ellipse 30% 35% at 15% 45%, #ecc79a 0%, transparent 75%),
      linear-gradient(160deg, var(--cream) 0%, var(--blush) 40%, #f6e2cf 70%, #f9f2ea 100%);
  }

  .script {
    position: absolute;
    margin: 0;
    font-family: "Homemade Apple", cursive;
    color: var(--ink);
    white-space: nowrap;
    line-height: 1;
    font-weight: 400;
  }
  .headline { left: 150px; top: 88px; font-size: 44px; }
  .ribbon {
    position: absolute;
    left: 150px;
    top: 154px;
    width: 204px;
    height: 42px;
  }
  .ribbon-text { left: 176px; top: 160px; font-size: 22px; }
  .name-first { left: 30px; top: 268px; font-size: 58px; }
  .conjunction { left: 220px; top: 352px; font-size: 32px; }
  .name-second { left: 268px; top: 420px; font-size: 58px; }
  .date { left: 172px; top: 576px; font-size: 24px; }
  .rule {
    position: absolute;
    left: 140px;
    top: 628px;
    width: 226px;
    height: 2px;
    background: var(--ink);
  }

  .frame {
    position: absolute;
    left: 35px;
    top: 41px;
    width: 453px;
    height: 599px;
  }
  .thanks-text {
    position: absolute;
    left: 0;
    right: 0;
    top: 360px;
    margin: 0;
    text-align: center;
    font-family: "Great Vibes", cursive;
    font-weight: 400;
    font-size: 66px;
    color: var(--ink);
    line-height: 1;
  }
</style>
</head>
<body>
<main class="canvas">
  <section class="label label--wedding">
    <div class="wedding-art" role="img" aria-label="Watercolour roses in pink and peach framing top and bottom over pastel washes of blue and yellow"></div>
    <h1 class="script headline">Specially</h1>
    <svg class="ribbon" viewBox="0 0 204 42" aria-hidden="true">
      <polygon points="4,0 200,0 192,21 204,42 0,42 8,21" fill="var(--ribbon)" opacity="0.9"/>
    </svg>
    <p class="script ribbon-text">bottled for</p>
    <p class="script name-first">Elena</p>
    <p class="script conjunction">and</p>
    <p class="script name-second">Marco</p>
    <p class="script date">July 16,2018.</p>
    <div class="rule"></div>
  </section>

  <section class="label label--thanks">
    <div class="thanks-art" role="img" aria-label="Abstract painted brushstrokes in blush, cream, gold and mint"></div>
    <svg class="frame" viewBox="0 0 453 599" aria-hidden="true">
      <rect x="2.5" y="2.5" width="448" height="594" fill="none" stroke="var(--ink)" stroke-width="5"/>
      <rect x="9" y="9" width="435" height="581" fill="none" stroke="var(--ink)" stroke-width="1.5"/>
    </svg>
    <h2 class="thanks-text">Thank You</h2>
  </section>
</main>
</body>
</html>
```